Want a DL Flyer designed for mailout, with the following info. Please see the website www.ledgerbrightco.com.au for any other info.
Content:
EVERYTHING YOU NEED FROM AN ACCOUNTANT
(tick) Value for money
(tick) Mobile visits to your farm or business
(tick) Fixed Fees Agreed Upfront
(tick) Advice tailored to your circumstances
(tick) Help to grow your business
(tick) Talk directly to your accountant, the person who knows you
(tick) Small business & Primary Producer Specialists
+ MORE.......TALLYWELL GROUP. YOU'RE MORE THAN A NUMBER WITH US.
Director: Gordon Pellew CPA | Associate: Soraya Finch CPA
Call (07) 4519 2386 www.ledgerbrightco.com.au PO Box 827 Dalby Qld 4405

```html
<!DOCTYPE html>
<html lang="en">
<head>
<meta charset="utf-8">
<title>Tallywell Group DL Flyer</title>
<link rel="stylesheet" href="https://fonts.googleapis.com/css2?family=Anton&family=Montserrat:wght@600;700;800&family=Roboto:wght@400;500;700&family=Roboto+Condensed:wght@700&display=swap">
<style>
:root{
  --backdrop:#404040;
  --paper:#ffffff;
  --brand-red:#c8161d;
  --ink:#111111;
  --grey:#8c8c8c;
  --photo-blue:#6f9ac4;
  --photo-light:#dfe9f3;
  --photo-dark:#2c3f5c;
  --rule:#333333;
  --stamp:#dcdcdc;
}
*{margin:0;padding:0;box-sizing:border-box}
html,body{width:1200px;height:1200px;overflow:hidden;background:var(--backdrop)}
.canvas{position:relative;width:1200px;height:1200px}

/* Front (portrait DL) */
.front{position:absolute;left:66px;top:215px;width:338px;height:695px;background:var(--paper);overflow:hidden}
.front .brand{position:absolute;top:28px;left:0;width:100%;text-align:center}
.front .brand-square{display:block;width:46px;height:46px;margin:0 auto 24px;background:var(--brand-red)}
.front .brand-name{font-family:"Montserrat",sans-serif;font-weight:700;font-size:26px;color:var(--brand-red);letter-spacing:-.3px}
.front .headline{position:absolute;top:146px;left:0;width:100%;text-align:center;font-family:"Anton",sans-serif;font-size:55px;line-height:1;color:var(--brand-red);letter-spacing:.5px}
.front .subline{position:absolute;top:204px;left:0;width:100%;text-align:center;font-family:"Montserrat",sans-serif;font-weight:800;font-size:20px;color:var(--ink)}
.front .photo{position:absolute;top:230px;left:0;width:100%;height:371px;background:linear-gradient(160deg,var(--photo-light) 0%,var(--photo-blue) 45%,var(--photo-dark) 100%)}
.front .call-band{position:absolute;top:601px;left:0;width:100%;height:42px;background:var(--brand-red);color:#fff;font-family:"Montserrat",sans-serif;font-weight:700;font-size:21px;display:flex;align-items:center;justify-content:center}
.front .web-band{position:absolute;top:643px;left:0;width:100%;height:52px;background:var(--ink);color:#fff;font-family:"Montserrat",sans-serif;font-weight:600;font-size:12.5px;display:flex;align-items:center;justify-content:center;gap:6px}

/* Back (landscape DL) */
.back{position:absolute;left:436px;top:474px;width:695px;height:337px;background:var(--paper);overflow:hidden}
.back .photo{position:absolute;left:0;top:172px;width:265px;height:165px;background:linear-gradient(90deg,var(--photo-dark) 0%,var(--photo-blue) 45%,rgba(255,255,255,0) 100%)}
.back .title{position:absolute;left:19px;top:14px;font-family:"Roboto Condensed",sans-serif;font-weight:700;font-size:21.5px;color:var(--brand-red);white-space:nowrap}
.back .benefits{position:absolute;left:19px;top:38px;list-style:none;font-family:"Roboto",sans-serif;font-size:13px;color:var(--ink)}
.back .benefits li{height:19.2px;display:flex;align-items:center;gap:9px;white-space:nowrap}
.back .benefits svg{flex:none}
.back .brand{position:absolute;left:356px;top:46px;width:140px;text-align:center}
.back .brand-square{display:block;width:22px;height:22px;margin:0 auto 6px;background:var(--brand-red)}
.back .brand-name{font-family:"Roboto",sans-serif;font-weight:500;font-size:12px;color:var(--brand-red)}
.back .more{position:absolute;left:142px;top:173px;font-family:"Roboto",sans-serif;font-weight:500;font-size:16px;line-height:18.5px;color:var(--brand-red);white-space:nowrap}
.back .people{position:absolute;left:187px;top:215px;font-family:"Roboto",sans-serif;font-size:18px;line-height:24px;color:var(--ink);white-space:nowrap}
.back .people b{color:var(--brand-red);font-weight:700}
.back .call{position:absolute;left:189px;top:265px;font-family:"Montserrat",sans-serif;font-weight:700;font-size:21px;color:var(--ink)}
.back .contact{position:absolute;left:192px;top:291px;font-family:"Roboto",sans-serif;color:var(--ink)}
.back .contact p{display:flex;align-items:center;gap:5px;white-space:nowrap}
.back .contact .web{font-size:13px;font-weight:500;height:17px}
.back .contact .post{font-size:10px;font-weight:500;height:17px}
.back .stamp{position:absolute;left:615px;top:24px;width:50px;height:50px;background:var(--stamp)}
.back .address-line{position:absolute;left:508px;width:162px;height:1px;background:var(--rule)}
</style>
</head>
<body>
<div class="canvas">

  <section class="front">
    <div class="brand">
      <span class="brand-square"></span>
      <span class="brand-name">Tallywell Group</span>
    </div>
    <h1 class="headline">YOU ARE NOT</h1>
    <p class="subline">JUST A NUMBER WITH US</p>
    <div class="photo" role="img" aria-label="Photo of a smiling businesswoman shaking hands with a client in a bright office"></div>
    <div class="call-band">Call (07) 4519 2386</div>
    <div class="web-band">
      <svg width="11" height="11" viewBox="0 0 12 12" aria-hidden="true"><circle cx="6" cy="6" r="5" fill="none" stroke="#c8161d" stroke-width="1.3"/><ellipse cx="6" cy="6" rx="2.2" ry="5" fill="none" stroke="#c8161d" stroke-width="1"/><line x1="1" y1="6" x2="11" y2="6" stroke="#c8161d" stroke-width="1"/></svg>
      www.ledgerbrightco.com.au
    </div>
  </section>

  <section class="back">
    <div class="photo" role="img" aria-label="Photo of two businessmen reviewing documents at a desk"></div>
    <h2 class="title">EVERYTHING YOU NEED FROM AN ACCOUNTANT</h2>
    <ul class="benefits">
      <li><svg width="13" height="13" viewBox="0 0 14 14" aria-hidden="true"><circle cx="7" cy="7" r="7" fill="#c8161d"/><path d="M3.8 7.2l2.2 2.2 4.3-4.6" fill="none" stroke="#fff" stroke-width="1.8"/></svg>Value for money</li>
      <li><svg width="13" height="13" viewBox="0 0 14 14" aria-hidden="true"><circle cx="7" cy="7" r="7" fill="#c8161d"/><path d="M3.8 7.2l2.2 2.2 4.3-4.6" fill="none" stroke="#fff" stroke-width="1.8"/></svg>Mobile visits to your farm or business</li>
      <li><svg width="13" height="13" viewBox="0 0 14 14" aria-hidden="true"><circle cx="7" cy="7" r="7" fill="#c8161d"/><path d="M3.8 7.2l2.2 2.2 4.3-4.6" fill="none" stroke="#fff" stroke-width="1.8"/></svg>Fixed Fees Agreed Upfront</li>
      <li><svg width="13" height="13" viewBox="0 0 14 14" aria-hidden="true"><circle cx="7" cy="7" r="7" fill="#c8161d"/><path d="M3.8 7.2l2.2 2.2 4.3-4.6" fill="none" stroke="#fff" stroke-width="1.8"/></svg>Advice tailored to your circumstances</li>
      <li><svg width="13" height="13" viewBox="0 0 14 14" aria-hidden="true"><circle cx="7" cy="7" r="7" fill="#c8161d"/><path d="M3.8 7.2l2.2 2.2 4.3-4.6" fill="none" stroke="#fff" stroke-width="1.8"/></svg>Help to grow your business</li>
      <li><svg width="13" height="13" viewBox="0 0 14 14" aria-hidden="true"><circle cx="7" cy="7" r="7" fill="#c8161d"/><path d="M3.8 7.2l2.2 2.2 4.3-4.6" fill="none" stroke="#fff" stroke-width="1.8"/></svg>Talk directly to your accountant, the person who knows you</li>
      <li><svg width="13" height="13" viewBox="0 0 14 14" aria-hidden="true"><circle cx="7" cy="7" r="7" fill="#c8161d"/><path d="M3.8 7.2l2.2 2.2 4.3-4.6" fill="none" stroke="#fff" stroke-width="1.8"/></svg>Small business &amp; Primary Producer Specialists</li>
    </ul>
    <div class="brand">
      <span class="brand-square"></span>
      <span class="brand-name">Tallywell Group</span>
    </div>
    <p class="more">+ MORE.......TALLYWELL GROUP.<br>YOU'RE MORE THAN A NUMBER WITH US.</p>
    <p class="people"><b>Director:</b> Gordon Pellew CPA<br><b>Associate:</b> Soraya Finch CPA</p>
    <p class="call">Call (07) 4519 2386</p>
    <div class="contact">
      <p class="web"><svg width="11" height="11" viewBox="0 0 12 12" aria-hidden="true"><circle cx="6" cy="6" r="5" fill="none" stroke="#c8161d" stroke-width="1.3"/><ellipse cx="6" cy="6" rx="2.2" ry="5" fill="none" stroke="#c8161d" stroke-width="1"/><line x1="1" y1="6" x2="11" y2="6" stroke="#c8161d" stroke-width="1"/></svg>www.ledgerbrightco.com.au</p>
      <p class="post"><svg width="11" height="12" viewBox="0 0 10 12" aria-hidden="true"><path d="M5 0a4 4 0 0 1 4 4c0 3-4 8-4 8S1 7 1 4a4 4 0 0 1 4-4z" fill="#c8161d"/><circle cx="5" cy="4" r="1.5" fill="#fff"/></svg>PO Box 827 Dalby Qld 4405</p>
    </div>
    <div class="stamp"></div>
    <div class="address-line" style="top:138px"></div>
    <div class="address-line" style="top:161px"></div>
    <div class="address-line" style="top:183px"></div>
  </section>

</div>
</body>
</html>
```